VoRuBel Estates (New Napa Valley Cabernet) Website Design

We need a website design for our new company, VoRuBel Estates and the launch of our inaugural vintage of VoRuBel Napa Valley Cabernet. Here is our story:

2009 Napa Valley Cabernet Sauvignon
VoRuBel
Three friends, a passion for wine and a love of creating together fueled our development of VoRuBel Cabernet. As with most ardent endeavors, VoRuBel has been a project requiring the ultimate in patience, perseverance and commitment.

Our brand, VoRuBel is the phonetic spelling of our initials – Tessa, Lorna, and Stuart - and is pronounced VRB. Our logo, three wine glasses entwined, is the symbol of our friendship, the celebration of our families and our toast to the passionate desire to create remarkable wines from Napa Valley.

In every bottle of VoRuBel Cabernet Sauvignon, we hope you taste not only the richness and balanced flavors of the wine, but also the bond of our friendship.

From Tessa, Lorna and Stuart . . .
“We toast to all of life’s moments with you!”

We are launching our website and the eCom sales of our wine in October 2012. The website is our only means for soliciting orders. We have a bottle shot, a logo, some pictures and a wire frame and content draft. The wine is labeled and approved. We do not have a look, feel or architecture for our website. We will be making additional wines in the future but currently are releasing our 2009 VoRuBel Napa Valley Cabernet.

We are required to provide layered photo shop or word press design files to our eCom platform provider.

Thanks for your interest and ideas.

Wine drinkers, likely baby boomer age, largely CA located, higher income

Architecture

Must have
• Must have a store
Prefer not to reverse out the logo
Home page should feature some pictures, not heavy text

```html
<!DOCTYPE html>
<html lang="en">
<head>
<meta charset="utf-8">
<title>VoRuBel Estates — Home</title>
<link href="https://fonts.googleapis.com/css2?family=Great+Vibes&family=Arimo:ital,wght@0,400;0,700;1,400&display=swap" rel="stylesheet">
<style>
  :root{
    --wine:#5a0e1e;
    --wine-dark:#3c0612;
    --wine-mid:#7a1a2c;
    --tan:#b99558;
    --tan-light:#d6b97f;
    --parchment:#e9d8b0;
    --card:#fbf7ee;
    --card-edge:#a8844c;
    --ink:#2f241c;
    --muted:#6b5a48;
    --photo-warm:#8a5a3c;
    --photo-deep:#3b2418;
    --sky:#d7e6ef;
    --sky-edge:#8fb0c4;
  }
  *{box-sizing:border-box;margin:0;padding:0}
  html,body{width:863px;height:1200px;overflow:hidden}
  body{background:radial-gradient(ellipse at 50% 40%,var(--wine-mid),var(--wine-dark));font-family:"Arimo",Arial,sans-serif;color:var(--ink);position:relative}
  .page-panel{position:absolute;left:10px;top:86px;width:843px;height:1070px;background:linear-gradient(180deg,var(--tan-light),var(--tan));border-radius:4px}
  .nav-band{position:absolute;left:10px;top:58px;width:843px;height:28px;background:linear-gradient(180deg,var(--parchment),var(--tan-light));border-bottom:2px solid var(--card-edge)}
  .nav{position:absolute;top:56px;display:flex;gap:30px;font-family:"Great Vibes",cursive;font-size:23px;color:var(--wine)}
  .nav a{color:inherit;text-decoration:none}
  .nav-left{left:40px}
  .nav-right{right:40px}
  .nav .current{color:var(--card);text-shadow:0 0 2px var(--wine)}
  .brand{position:absolute;left:288px;top:0;width:287px;height:70px;background:var(--card);border:3px solid var(--wine);border-top:none;display:flex;align-items:center;justify-content:center;box-shadow:0 2px 6px rgba(0,0,0,.4)}
  .brand span{font-family:"Great Vibes",cursive;font-size:44px;color:var(--wine)}
  .card{position:absolute;background:var(--card);border:3px solid var(--card-edge);box-shadow:0 2px 5px rgba(0,0,0,.35)}
  .card-title{font-family:"Great Vibes",cursive;font-weight:400;color:var(--wine);text-align:center;font-size:26px;display:flex;align-items:center;justify-content:center;gap:8px}
  .card-title::before,.card-title::after{content:"";flex:1;height:1px;background:var(--card-edge)}
  .read-more{font-family:"Great Vibes",cursive;color:var(--wine);font-size:22px;position:absolute}
  .body-text{font-size:11.5px;line-height:1.35;color:var(--ink)}
  .bottle{position:absolute;background:linear-gradient(90deg,#1b0a0c,#4a1820 45%,#1b0a0c);border-radius:10px 10px 3px 3px}
  .photo{position:absolute;background:linear-gradient(135deg,var(--photo-warm),var(--photo-deep))}

  .story{left:23px;top:100px;width:193px;height:260px;padding:8px 10px}
  .story .body-text{margin-top:4px;font-size:10px;line-height:1.3}
  .story .bottle{left:138px;top:190px;width:22px;height:60px}
  .story .read-more{left:28px;top:214px}

  .mailing{position:absolute;left:245px;top:216px;width:172px;height:115px;text-align:center}
  .mailing h3{font-family:"Great Vibes",cursive;font-weight:400;font-size:21px;color:var(--wine)}
  .mailing p{font-family:"Great Vibes",cursive;font-size:17px;color:var(--wine-mid);line-height:1}
  .mailing .field{margin:6px auto 0;width:150px;height:22px;background:var(--card);border:1px solid var(--card-edge);font-size:11px;text-align:left;padding:4px 6px;color:var(--muted)}

  .hero-photo{left:432px;top:100px;width:402px;height:245px;border:3px solid var(--card);box-shadow:0 2px 5px rgba(0,0,0,.35);background:linear-gradient(160deg,#c9c0b3,#7b5a46 55%,#3a2619)}

  .events{left:23px;top:374px;width:509px;height:475px;padding:8px 14px}
  .events .lead-photo{left:12px;top:42px;width:267px;height:202px;background:linear-gradient(135deg,#b5704a,#5c2a1c)}
  .events .lead-text{position:absolute;left:292px;top:42px;width:200px;font-size:11px;line-height:1.33}
  .events .thumbs{position:absolute;left:12px;top:258px;display:flex;gap:8px}
  .events .thumbs div{width:91px;height:68px;background:linear-gradient(135deg,var(--photo-warm),var(--photo-deep))}
  .events blockquote{position:absolute;left:16px;top:350px;width:470px;font-style:italic;font-size:14px;line-height:1.35;color:var(--ink)}
  .events .read-more{right:22px;top:432px}

  .product{left:547px;top:532px;width:287px;height:216px;padding:8px 12px}
  .product .bottle{left:18px;top:48px;width:30px;height:110px}
  .product .body-text{position:absolute;left:68px;top:48px;width:205px}
  .product .read-more{right:20px;top:176px}

  .social-feed{position:absolute;left:575px;top:762px;width:259px;height:331px;background:var(--card);border:3px solid var(--sky-edge)}
  .feed-head{height:36px;background:linear-gradient(180deg,#eef5f9,var(--sky));padding:6px 10px;font-size:16px;font-weight:700;color:#3b6f8f}
  .tweet{display:flex;gap:8px;padding:7px 10px;border-bottom:1px solid #e2e8ec;font-size:10px;line-height:1.3}
  .tweet .avatar{flex:none;width:32px;height:32px;background:linear-gradient(135deg,#9a7b62,#4e3527)}
  .tweet b{color:#3b6f8f}
  .feed-foot{position:absolute;bottom:8px;right:10px;display:flex;gap:5px}
  .feed-foot span{width:18px;height:18px;border-radius:3px;background:var(--sky-edge)}

  .motto{left:23px;top:863px;width:509px;height:173px;display:flex;flex-direction:column;align-items:center;justify-content:center;font-family:"Great Vibes",cursive;color:var(--wine);font-size:50px;line-height:1.05;text-align:center}

  .like-bar{position:absolute;left:23px;top:1050px;width:509px;height:58px;background:var(--card);border:3px solid var(--card-edge);display:flex;align-items:center;gap:10px;padding:0 12px;font-size:12px}
  .like-bar .brand-name{font-weight:700;color:var(--ink)}
  .like-bar .btn{background:#e4e7ee;border:1px solid #b7bdcc;padding:2px 7px;font-size:11px}
  .like-bar .faces{display:flex;gap:4px;margin-left:auto}
  .like-bar .faces div{width:26px;height:26px;background:linear-gradient(135deg,#a38670,#55392a)}

  .footer-nav{position:absolute;right:22px;top:1112px;display:flex;gap:13px;font-family:"Great Vibes",cursive;font-size:19px;color:var(--wine)}
  .footer-nav a{color:inherit;text-decoration:none}
  .copyright{position:absolute;left:14px;top:1168px;font-size:10px;color:var(--parchment)}
</style>
</head>
<body>
  <div class="nav-band"></div>
  <nav class="nav nav-left"><a class="current">Home</a><a>About</a><a>Gallery</a></nav>
  <nav class="nav nav-right"><a>Order</a><a>News</a><a>Contact</a></nav>
  <div class="page-panel"></div>
  <header class="brand"><span>VoRuBel</span></header>

  <section class="card story">
    <h2 class="card-title">Our Story</h2>
    <p class="body-text">Three friends, a passion for wine and a love of working and creating together fueled the ultimate development and launch of VoRuBel Estates.<br><br>As with most passionate and creative endeavors, VoRuBel has been a project requiring patience, perseverance, commitment and satisfying results.</p>
    <span class="read-more">Read More</span>
    <div class="bottle" role="img" aria-label="VoRuBel Cabernet bottle"></div>
  </section>

  <form class="mailing">
    <h3>Join Our Mailing List</h3>
    <p>Special Deals and<br>Release Information</p>
    <div class="field">Name</div>
    <div class="field">Email</div>
  </form>

  <div class="photo hero-photo" role="img" aria-label="Photo of wine glasses and bottles on a vineyard table"></div>

  <section class="card events">
    <h2 class="card-title">Recent Events and News</h2>
    <div class="photo lead-photo" role="img" aria-label="Photo of a wine tasting event"></div>
    <p class="body-text lead-text">Lorem ipsum dolor sit amet, consectetur adipisicing elit, sed do eiusmod tempor incididunt ut labore et dolore magna aliqua. Ut enim ad minim veniam, quis nostrud exercitation ullamco laboris nisi ut aliquip ex ea commodo consequat. Lorem ipsum dolor sit amet, consectetur adipisicing elit, sed do eiusmod tempor incididunt ut labore et dolore magna aliqua. Ut enim ad minim veniam, quis nostrud exercitation ullamco.</p>
    <div class="thumbs" role="img" aria-label="Event photo thumbnails"><div></div><div></div><div></div><div></div><div></div></div>
    <blockquote>“Lorem ipsum dolor sit amet, consectetur adipisicing elit, sed do eiusmod tempor incididunt ut labore et dolore magna aliqua.”</blockquote>
    <span class="read-more">Read More</span>
  </section>

  <section class="card product">
    <h2 class="card-title">New Product</h2>
    <div class="bottle" role="img" aria-label="VoRuBel Napa Valley Cabernet bottle"></div>
    <p class="body-text">Lorem ipsum dolor sit amet, consectetur adipisicing elit, sed do eiusmod tempor incididunt ut labore et dolore magna aliqua. Ut enim ad minim veniam, quis nostrud exercitation ullamco laboris nisi ut aliquip ex ea commodo consequat.</p>
    <span class="read-more">Learn More</span>
  </section>

  <aside class="social-feed">
    <div class="feed-head">Chirper</div>
    <div class="tweet"><div class="avatar" role="img" aria-label="Profile photo"></div><p><b>VoRuBel Estates</b><br>New vintage notes are up on our blog today</p></div>
    <div class="tweet"><div class="avatar" role="img" aria-label="Profile photo"></div><p><b>VoRuBel Estates</b><br>Thank you to everyone at last night's tasting</p></div>
    <div class="tweet"><div class="avatar" role="img" aria-label="Profile photo"></div><p><b>VoRuBel Estates</b><br>Harvest is starting early in the valley this year</p></div>
    <div class="tweet"><div class="avatar" role="img" aria-label="Profile photo"></div><p><b>VoRuBel Estates</b><br>Pairing tips for a cool autumn evening</p></div>
    <div class="feed-foot"><span></span><span></span><span></span></div>
  </aside>

  <section class="card motto">
    <span>Motto and Slogan -</span>
    <span>Here's The Slogan!</span>
  </section>

  <div class="like-bar">
    <span class="brand-name">FriendWall</span>
    <span class="btn">Like</span>
    <span>105,572 people like this.</span>
    <div class="faces" role="img" aria-label="Profile photos of fans"><div></div><div></div><div></div><div></div><div></div></div>
  </div>

  <nav class="footer-nav"><a>Home</a><a>About</a><a>Gallery</a><a>Order</a><a>News</a><a>Contact</a></nav>
  <p class="copyright">Copyright ©2012 VoRuBel. All Rights Reserved.</p>
</body>
</html>
```